Ductless Mini Split Business Website

Tall Fern Services is looking to design an eye catching educational website about installing Ductless mini splits.

Similar to this company.
https://www.kelvarocomfort.com/

```html
<!DOCTYPE html>
<html lang="en">
<head>
<meta charset="utf-8">
<title>Tall Fern Services – Ductless Mini Split Experts</title>
<link href="https://fonts.googleapis.com/css2?family=Righteous&family=Montserrat:wght@400;500;600;700&display=swap" rel="stylesheet">
<style>
:root{
  --yellow:#ffd600;
  --gold:#f1b80d;
  --gold-deep:#e3a80b;
  --ink:#111111;
  --text:#222222;
  --muted:#555555;
  --white:#ffffff;
  --hero-a:#c9d0d4;
  --hero-b:#5d6a73;
}
*{box-sizing:border-box;margin:0;padding:0}
html,body{width:1200px;height:4873px;overflow:hidden;background:var(--white)}
body{font-family:"Montserrat",sans-serif;color:var(--text);position:relative}
.abs{position:absolute}
.display{font-family:"Righteous",sans-serif;color:var(--ink);text-transform:uppercase;line-height:1.02}
.btn{position:absolute;display:flex;align-items:center;justify-content:center;border:2px solid var(--ink);font-weight:700;font-size:13px;color:var(--ink);background:var(--white);text-transform:uppercase}
.hex{position:absolute;clip-path:polygon(50% 0,100% 25%,100% 75%,50% 100%,0 75%,0 25%)}
.photo-a{background:linear-gradient(135deg,#dfe6ea,#8e9ba4)}
.photo-b{background:linear-gradient(135deg,#f1ede6,#b8a995)}
.photo-c{background:linear-gradient(135deg,#e8edf0,#4d6678)}
.mascot{position:absolute;border-radius:50%;background:radial-gradient(circle at 45% 45%,#ffe04a,#e0a800 60%,#1a1a1a 100%)}
/* header */
.topbar{left:715px;top:0;width:485px;height:44px;background:var(--ink);color:var(--white);font-size:17px;display:flex;align-items:center;padding-left:14px;gap:6px}
.topbar b{color:var(--yellow);font-weight:600}
.nav{left:520px;top:44px;width:525px;height:44px;background:var(--white);display:flex;align-items:center;justify-content:space-around;font-size:14px;color:var(--ink)}
.brand{left:156px;top:22px;display:flex;align-items:center;gap:10px;font-weight:700;font-size:24px;color:var(--ink)}
.brand i{display:block;width:34px;height:34px;border-radius:50%;background:var(--gold)}
.brand-sub{left:162px;top:88px;font-weight:700;font-size:20px;color:#6b4a00;letter-spacing:.5px}
/* section heading */
.h2{font-family:"Righteous",sans-serif;color:var(--ink);text-align:center;width:100%;font-size:46px}
.tag{position:absolute;height:40px;background:var(--yellow);display:flex;align-items:center;justify-content:center;font-weight:700;font-size:15px;color:var(--ink)}
.body-copy{font-size:14px;line-height:1.55;color:var(--text)}
.feature h4{font-size:19px;font-weight:700;color:var(--ink);margin-bottom:8px}
.feature p{font-size:13px;line-height:1.45;color:var(--muted)}
.feat-icon{width:104px;height:116px;background:var(--gold);display:flex;align-items:center;justify-content:center}
.field{position:absolute;left:757px;width:286px;height:38px;border:1px solid #cfcfcf;font-size:11px;color:#666;padding:10px 12px}
.footer{left:0;top:4411px;width:1200px;height:426px;background:var(--ink);color:var(--white)}
.footer h5{font-size:18px;font-weight:700;margin-bottom:26px}
.footer li{list-style:none;font-size:14px;margin-bottom:14px}
.social{width:40px;height:40px;border-radius:50%;background:var(--yellow)}
</style>
</head>
<body>

<!-- HERO -->
<section class="abs" style="left:0;top:0;width:1200px;height:644px;background:linear-gradient(100deg,#f3f5f6 0%,#dfe3e5 35%,var(--hero-b) 100%)">
  <div class="abs" role="img" aria-label="Woman relaxing on a sofa pointing a remote at a wall-mounted ductless unit" style="left:430px;top:0;width:770px;height:644px;background:linear-gradient(110deg,rgba(255,255,255,0) 0%,#8c979e 40%,#46535c 100%)"></div>
  <div class="abs" role="img" aria-label="Wall-mounted mini split indoor unit" style="left:545px;top:92px;width:250px;height:80px;background:linear-gradient(#ffffff,#d8dde0);border-radius:6px"></div>
  <div class="mascot" role="img" aria-label="Cartoon bee mascot holding a wrench" style="left:330px;top:158px;width:150px;height:130px"></div>
</section>
<div class="abs topbar">&#9742; Call Us Toll Free: <b>+1 (555) 014 2727</b></div>
<nav class="abs nav"><span>About</span><span>Ductless Mini Split</span><span>Faq</span><span>Financing</span><span>Reviews</span><span>Contact</span></nav>
<div class="abs brand"><i></i>Tall Fern Services</div>
<div class="abs brand-sub">DUCTLESS EXPERTS</div>
<h1 class="abs display" style="left:160px;top:262px;font-size:46px;width:420px">Ductless<br>Mini Split<br>Business</h1>
<p class="abs body-copy" style="left:162px;top:412px;width:300px;font-size:13.5px;line-height:1.45">Lorem ipsum dolor sit amet, consectetur adipiscing elit. Integer sed dapibusctus eget molestie felis.</p>
<div class="btn" style="left:162px;top:486px;width:136px;height:38px;background:transparent">Find Out More</div>
<svg class="abs" style="left:160px;top:550px" width="64" height="28" viewBox="0 0 64 28" fill="none" stroke="#111" stroke-width="2"><circle cx="14" cy="14" r="11"/><path d="M16 9l-5 5 5 5"/><circle cx="48" cy="14" r="11"/><path d="M46 9l5 5-5 5"/></svg>

<!-- HELP -->
<h2 class="abs h2" style="left:0;top:722px">How Can We Help You?</h2>
<div class="hex photo-c" role="img" aria-label="Technician replacing an outdoor unit" style="left:178px;top:805px;width:166px;height:190px"></div>
<div class="hex photo-a" role="img" aria-label="Technician remodelling an indoor unit" style="left:404px;top:805px;width:166px;height:190px"></div>
<div class="hex photo-a" role="img" aria-label="Hands installing an indoor unit" style="left:629px;top:805px;width:166px;height:190px"></div>
<div class="hex photo-c" role="img" aria-label="Maintenance on an open indoor unit" style="left:854px;top:805px;width:166px;height:190px"></div>
<div class="tag" style="left:157px;top:1006px;width:208px">REPLACEMENT</div>
<div class="tag" style="left:383px;top:1006px;width:208px">REMODELS</div>
<div class="tag" style="left:608px;top:1006px;width:210px">INSTALLATION</div>
<div class="tag" style="left:833px;top:1006px;width:210px">MAINTENANCE</div>
<div class="btn" style="left:458px;top:1075px;width:284px;height:42px">More Tall Fern Services</div>

<!-- ABOUT -->
<div class="abs" style="left:0;top:1203px;width:585px;height:6px;background:var(--gold)"></div>
<div class="abs" style="left:579px;top:1203px;width:6px;height:540px;background:var(--gold)"></div>
<div class="abs" style="left:585px;top:1242px;width:615px;height:556px;background:linear-gradient(120deg,var(--yellow),#f6d52d)"></div>
<div class="hex photo-a" role="img" aria-label="Technician working on a ceiling cassette" style="left:878px;top:1188px;width:180px;height:204px"></div>
<div class="hex photo-c" role="img" aria-label="Technician cleaning the filter of an indoor unit" style="left:612px;top:1290px;width:432px;height:498px"></div>
<div class="hex photo-a" role="img" aria-label="Technician servicing a wall unit" style="left:588px;top:1680px;width:180px;height:204px"></div>
<p class="abs" style="left:157px;top:1296px;font-size:22px;letter-spacing:1px">ABOUT US</p>
<h2 class="abs display" style="left:157px;top:1326px;font-size:40px;width:440px">Meet Our<br>Tall Fern Services<br>Experts</h2>
<p class="abs body-copy" style="left:157px;top:1456px;width:360px;font-size:13.5px;line-height:1.55">Lorem ipsum dolor sit amet, consectetur adipiscing elit. Vivamus facilisis metus lacus, non posuere nulla porta eget. Duis sem ipsum, sollicitudin ac nisl ut, posuere molestie orci. In euismod lorem et orci auctor scelerisque. Curabitur euismod tortor quis magna gravida, nec suscipit turpis ultrices. Sed id condimentum tellus, sit amet facilisis purus. Nam non finibus velit.</p>
<div class="btn" style="left:157px;top:1650px;width:136px;height:40px">Read More</div>

<!-- CALL BAR -->
<div class="mascot" role="img" aria-label="Cartoon bee mascot with a wrench" style="left:150px;top:1772px;width:236px;height:186px"></div>
<div class="abs" style="left:150px;top:1954px;width:901px;height:76px;background:var(--ink)"></div>
<svg class="abs" style="left:150px;top:1954px" width="540" height="76"><polygon points="0,0 540,0 530,0 470,76 0,76" fill="var(--gold)"/><polygon points="0,0 540,0 480,76 0,76" fill="var(--gold)"/></svg>
<p class="abs" style="left:168px;top:1970px;width:460px;font-size:14px;font-weight:600;color:var(--ink);line-height:1.4">Call Tall Fern Services for all of your air conditioning and indoor air quality needs</p>
<p class="abs" style="left:746px;top:1976px;font-size:21px;font-weight:700;color:var(--yellow)">&#9742; +1 (555) 014 2727</p>

<!-- WHY CHOOSE -->
<svg class="abs" style="left:0;top:2054px" width="560" height="682" role="img" aria-label="Worker in a hard hat and safety vest fitting an indoor unit"><defs><linearGradient id="why" x1="0" y1="0" x2="1" y2="1"><stop offset="0" stop-color="#eef0f0"/><stop offset="1" stop-color="#b9c25a"/></linearGradient></defs><polygon points="0,0 552,170 380,682 0,682" fill="var(--gold)"/><polygon points="0,14 536,178 360,676 0,676" fill="url(#why)"/></svg>
<h2 class="abs display" style="left:606px;top:2104px;font-size:40px">Why Choose<br>Tall Fern Services</h2>
<p class="abs body-copy" style="left:606px;top:2198px;width:420px;font-size:14px">Fusce maximus est mi. Cras sit amet odio turpis. Vestibulum ante ipsum primis in faucibus orci luctus et ultrices posuere cubilia Curae; Nulla ac eros in erat tincidunt</p>
<div class="abs hex feat-icon" style="left:607px;top:2322px"><svg width="44" height="44" viewBox="0 0 44 44" fill="none" stroke="#111" stroke-width="3"><rect x="8" y="6" width="28" height="32"/><path d="M14 14h16M14 21h16M14 28h10"/></svg></div>
<div class="abs feature" style="left:742px;top:2335px;width:310px"><h4>0% Financing for 60 months</h4><p>Duis volutpat dignissim elit, at tincidunt justo auctor ut. Suspendisse ornarehendrerit nulla nec dapibus.</p></div>
<div class="abs hex feat-icon" style="left:607px;top:2456px"><svg width="44" height="44" viewBox="0 0 44 44" fill="none" stroke="#111" stroke-width="3"><circle cx="22" cy="22" r="16"/><path d="M27 16c-2-2-9-2-9 2s9 3 9 7-7 4-10 2M22 11v22"/></svg></div>
<div class="abs feature" style="left:742px;top:2468px;width:310px"><h4>Money Back Guarantee</h4><p>Duis volutpat dignissim elit, at tincidunt justo auctor ut. Suspendisse ornarehendrerit nulla nec dapibus.</p></div>
<div class="abs hex feat-icon" style="left:607px;top:2588px"><svg width="44" height="44" viewBox="0 0 44 44" fill="#111"><circle cx="22" cy="20" r="6"/><path d="M10 38c0-8 5-12 12-12s12 4 12 12z"/><path d="M22 4l1.5 3 3 .4-2.2 2 .6 3-2.9-1.6-2.9 1.6.6-3-2.2-2 3-.4z"/></svg></div>
<div class="abs feature" style="left:742px;top:2600px;width:310px"><h4>We Are the Experts in<br>Ductless Services</h4><p>Duis volutpat dignissim elit, at tincidunt justo auctor ut. Suspendisse ornarehendrerit nulla nec dapibus.</p></div>

<!-- STAND BEHIND -->
<h2 class="abs h2" style="left:0;top:2812px;font-size:46px;line-height:1.05">WE STAND BEHIND OUR<br>TALL FERN SERVICES</h2>
<div class="abs" style="left:0;top:3214px;width:1200px;height:339px;background:linear-gradient(90deg,var(--gold-deep),var(--gold))"></div>
<div class="mascot" role="img" aria-label="Cartoon bee mascot" style="left:886px;top:2888px;width:206px;height:170px"></div>
<div class="hex photo-b" role="img" aria-label="Man adjusting an indoor unit" style="left:158px;top:3020px;width:226px;height:262px"></div>
<div class="hex photo-a" role="img" aria-label="Hands reviewing financing charts on a tablet" style="left:406px;top:2930px;width:388px;height:448px"></div>
<div class="hex photo-a" role="img" aria-label="Close-up of an indoor unit" style="left:816px;top:3020px;width:226px;height:262px"></div>
<p class="abs" style="left:158px;top:3297px;width:226px;text-align:center;font-weight:700;font-size:16px;color:var(--ink)">GET SOME ANSWER</p>
<div class="btn" style="left:214px;top:3336px;width:132px;height:38px;background:transparent">Our FAQ</div>
<p class="abs" style="left:816px;top:3297px;width:240px;text-align:center;font-weight:700;font-size:16px;color:var(--ink)">STAY UP TO DATE</p>
<div class="btn" style="left:872px;top:3336px;width:132px;height:38px;background:transparent">Our Blog</div>
<p class="abs" style="left:0;top:3393px;width:1200px;text-align:center;font-weight:700;font-size:22px;color:var(--ink)">OUR FINANCING OPTIONS</p>
<div class="btn" style="left:532px;top:3438px;width:136px;height:38px;background:transparent">Financing</div>

<!-- CONTACT -->
<div class="abs" role="img" aria-label="Technician kneeling beside an outdoor condenser unit" style="left:0;top:3553px;width:682px;height:520px;background:linear-gradient(120deg,#c9b79c,#8a8173 50%,#e6e3de)"></div>
<h2 class="abs display" style="left:757px;top:3614px;font-size:40px">Contact Us<br>Today</h2>
<div class="field" style="top:3733px">Name:</div>
<div class="field" style="top:3778px">Email:</div>
<div class="field" style="top:3823px">Phone No:</div>
<div class="field" style="top:3868px;height:88px">Comments:</div>
<div class="btn" style="left:757px;top:3973px;width:210px;height:40px">Send Information</div>

<!-- TESTIMONIAL -->
<div class="abs" style="left:150px;top:4073px;width:901px;height:20px;background:var(--ink)"></div>
<div class="abs" style="left:0;top:4363px;width:1200px;height:60px;background:var(--ink)"></div>
<div class="abs" style="left:150px;top:4090px;width:901px;height:322px;background:linear-gradient(180deg,var(--gold),var(--gold-deep))"></div>
<svg class="abs" style="left:156px;top:4132px" width="64" height="40" viewBox="0 0 64 40" fill="#111"><circle cx="14" cy="14" r="13"/><path d="M2 16c0 14 8 22 14 24l-2-10z"/><circle cx="46" cy="14" r="13"/><path d="M34 16c0 14 8 22 14 24l-2-10z"/></svg>
<p class="abs" style="left:232px;top:4132px;color:var(--white);font-size:16px;letter-spacing:2px">★★★★★</p>
<p class="abs" style="left:232px;top:4158px;width:770px;font-size:13.5px;line-height:1.6;color:var(--ink)">Duis volutpat dignissim elit, at tincidunt justo auctor ut. Suspendisse ornare hendrerit nulla nec dapibus. Fusce magna felis, ultricies a tempor eu, interdum eget urna. Nullam pulvinar lacus sit amet sem maximus pulvinar. Vivamus lacinia condimentum sapien id scelerisque. Vestibulum pulvinar metus non magna congue, et convallis justo suscipit. ”</p>
<p class="abs" style="left:232px;top:4280px;font-weight:600;font-size:15px;color:var(--ink)">- Vestibulum Ante</p>
<p class="abs" style="left:245px;top:4302px;font-size:12px;color:var(--ink)">Daucibus Orci</p>
<svg class="abs" style="left:232px;top:4338px" width="64" height="28" viewBox="0 0 64 28" fill="none" stroke="#111" stroke-width="2"><circle cx="14" cy="14" r="11"/><path d="M16 9l-5 5 5 5"/><circle cx="48" cy="14" r="11"/><path d="M46 9l5 5-5 5"/></svg>
<div class="mascot" role="img" aria-label="Cartoon bee mascot" style="left:944px;top:4240px;width:150px;height:150px"></div>

<!-- FOOTER -->
<footer class="abs footer">
  <div class="abs" style="left:156px;top:56px;display:flex;align-items:center;gap:10px;font-weight:700;font-size:20px;color:var(--yellow)"><span style="display:block;width:30px;height:30px;border-radius:50%;background:var(--gold)"></span>Tall Fern Services</div>
  <p class="abs" style="left:158px;top:100px;font-size:17px;font-weight:700;color:var(--gold)">DUCTLESS EXPERTS</p>
  <p class="abs" style="left:158px;top:141px;width:200px;font-size:12px;line-height:1.5">Vestibulum ante ipsum primis in faucibus orci luctus et ultrices posuere cubilia Curae; Nulla ac eros in erat tincidunt</p>
  <div class="abs" style="left:158px;top:250px;display:flex;gap:8px"><i class="social"></i><i class="social"></i><i class="social"></i></div>
  <div class="abs" style="left:432px;top:56px"><h5>Quick Links</h5><ul><li>Home</li><li>About Us</li><li>FAQ</li><li>Financing</li><li>Contact Us</li><li>Privacy Policy</li><li>Site Map</li></ul></div>
  <div class="abs" style="left:607px;top:56px;width:210px"><h5>Contact Info</h5>
    <div style="display:flex;gap:12px;font-size:13px;line-height:1.5;margin-bottom:14px"><span style="color:var(--yellow)">●</span><span>48, Larchmont Lane, 3rd floor, Fernvale, USA 2041</span></div>
    <div style="display:flex;gap:12px;font-size:13px;margin-bottom:18px"><span style="color:var(--yellow)">&#9742;</span><span>+1 (555) 014 2727</span></div>
    <div style="display:flex;gap:12px;font-size:13px;margin-bottom:18px"><span style="color:var(--yellow)">✉</span><span>Support@example.com</span></div>
    <div style="display:flex;gap:12px;font-size:13px;line-height:1.5"><span style="color:var(--yellow)">◷</span><span>Mon - Sat: 09.00am<br>to 18.00pm</span></div>
  </div>
  <div class="abs" style="left:833px;top:56px;width:210px"><h5>Subscribe Today</h5>
    <p style="font-size:13px;line-height:1.45;margin-bottom:16px">Subscribe us to get updates, news &amp; tips in your inbox.</p>
    <div style="height:34px;background:var(--white);color:#777;font-size:11px;padding:10px 18px;margin-bottom:6px">Enter your mail id:</div>
    <div style="height:34px;background:var(--yellow);color:var(--ink);font-weight:700;font-size:15px;display:flex;align-items:center;justify-content:center">Subscribe Now</div>
  </div>
</footer>
<div class="abs" style="left:0;top:4837px;width:1200px;height:36px;background:var(--gold);display:flex;align-items:center;justify-content:center;font-size:12px;color:var(--ink)">© 2019 Tall Fern Services. All rights reserved.</div>

</body>
</html>
```